Redo our website for our Robotics Northgrill

We sell robotic equipment to the restaurant industry. Our current robot, is a cooking robot that cooks up to 15 lbs of food. We will provide a prior website as well as brand guidelines. We plan on using wordpress and take advantage of wordpress's visual (no code) editor.

Current website - https://kelvatrix482.com/ (please note we are only selling Pindle now and no longer selling Quado+

We want someone to take our existing content and design the website as well as layout our content we provide. Here's a suggested site layout:

✅ KelvaTrix482 Website Wireframe / Site Map
1. Home

Purpose: Introduce Pindle, establish credibility, drive demo requests.

Sections:

Hero Section

Headline: “Meet Pindle — Your New Robotic Chef for High-Volume, Consistent Cooking.”

Sub-headline: Increase throughput. Reduce labor. Deliver perfect food every time.

CTA: Request a Demo + Watch Pindle Cook

Visual: Video loop or hero animation of Pindle in action.

How Pindle Works (3-4 steps)

Step cards: Load Ingredients → Select Recipe → Pindle Cooks → Serve

Icons and short explanations.

Key Benefits

Labor savings

Zero inconsistency

24/7 uptime

Throughput increases (30–50% faster)

Health & safety compliance

Who It’s For

QSR restaurants

Fast casual

Catering/commissaries

Ghost kitchens

Case Studies / Testimonials

Logo bar + quotes

“Pindle helped us reduce cooking times by 40%.”

Video Section

“Watch Pindle cook a full batch from start to finish.”

CTA Section

Big banner: Book a Demo

2. Product: “Meet Pindle”

Purpose: Deep dive into hardware, software, safety, reliability.

Sections:

Overview

What Pindle is

What tasks it automates

Where it fits in a kitchen

Hardware Features

High-temperature cooking chamber

Precision sensors

Automated stirring

Automated dispensing

Safety mechanisms (locking lids, auto-shutoff)

Software & AI

Recipe automation

IoT dashboard

Remote monitoring

Predictive maintenance

Specs Table

Dimensions

Power requirements

Capacity (lbs per batch)

Safety certifications

Gallery

Close-ups, installation photos, process shots

CTA: Request a Demo

3. Solutions

Purpose: Show that Pindle solves real operational problems.

Sub-pages or sections:

For Quick-Service Restaurants

Reduce labor cost

Speed up peak-hour demand

For Catering & Commissaries

Large-batch consistency

Automate repetitive cooking tasks

For High-Growth Chains

Replicable quality across multiple locations

Centralized recipe control

Each solution page includes:

A problem statement

How Pindle solves it

Metrics / KPIs

Relevant testimonial

CTA

4. ROI / Economics

Purpose: Sell the financial story clearly.

Sections:

Savings Calculator

Labor hours saved

Cost savings

Throughput increases

Food waste reduction

Before & After Comparison

Traditional kitchen vs. robotic kitchen

Sample ROI

“Payback in as little as 3–6 months.”

Download Full ROI Report (PDF)

5. Case Studies

Purpose: Social proof + real results.

Structure for each case study:

Customer background

Problem

Implementation

KPIs achieved

Labor savings

Consistency improvements

Cooking speed

Quote + photos/video

6. Pricing

Purpose: Start a commercial conversation.

Include:

Subscription model (monthly / annual)

Hardware leasing or purchase options

Installation + training

Support level

CTA to book a sales call

7. About

Purpose: Build trust.

Sections:

Mission statement

Founding team

Advisors/partners

“Why we built Pindle”

8. Resources

Purpose: SEO + education.

Subpages:

Blog (e.g., “The Future of Automated Kitchens”)

Whitepapers

Technical documentation

Product videos

9. Contact

General inquiry form

Sales contact

Support portal

Careers

```html
<!DOCTYPE html>
<html lang="en">
<head>
<meta charset="utf-8">
<title>KelvaTrix482 — Meet Pindle</title>
<link rel="stylesheet" href="https://fonts.googleapis.com/css2?family=Montserrat:wght@500;600;700;800&family=Oswald:wght@400;500&family=Source+Serif+4:ital,wght@0,400;1,400&family=Arimo:wght@400&display=swap">
<style>
:root{
  --navy:#0e2a4f;
  --navy-deep:#0b2342;
  --orange:#f04e23;
  --orange-light:#f47a40;
  --peach:#fde6e0;
  --white:#ffffff;
  --ink:#1d2433;
}
*{margin:0;padding:0;box-sizing:border-box}
html,body{width:1200px;height:4038px;overflow:hidden}
body{position:relative;background:var(--white);font-family:"Source Serif 4",serif;color:var(--ink)}
.abs{position:absolute}
.heading{font-family:"Montserrat",sans-serif;font-weight:700;color:var(--navy)}
.btn{position:absolute;display:flex;align-items:center;justify-content:center;border-radius:22px;font-family:"Montserrat",sans-serif;font-weight:700;font-size:16px;color:var(--white)}
.btn-orange{background:linear-gradient(90deg,var(--orange),var(--orange-light))}
.btn-navy{background:#2b5a92}

/* nav */
.site-nav{top:0;left:0;width:1200px;height:71px;background:var(--white)}
.brand{font-family:"Montserrat",sans-serif;font-weight:800;color:var(--orange);font-size:25px;letter-spacing:-0.5px}
.site-nav .brand{left:138px;top:21px}
.nav-links{left:339px;top:0;height:71px;display:flex;font-family:"Montserrat",sans-serif;font-size:13.5px;color:#333}
.nav-links span{display:flex;align-items:center;height:71px;padding:0 10px}
.nav-links .active{border-bottom:3px solid var(--orange);color:var(--orange)}

/* hero */
.page-bg-peach{top:600px;left:0;width:1200px;height:607px;background:var(--peach)}
.hero{top:71px;left:0;width:1200px;height:651px;background:linear-gradient(180deg,#2b4a74 0%,#34527c 40%,#20406a 100%);clip-path:polygon(0 0,100% 0,100% 532px,50% 651px,0 532px)}
.hero-title{top:290px;width:1200px;text-align:center;font-family:"Montserrat",sans-serif;font-weight:700;font-size:33px;line-height:37px;color:var(--white)}
.hero-sub{top:366px;width:1200px;text-align:center;font-family:"Oswald",sans-serif;font-size:18px;color:var(--white)}
.dots{top:588px;left:546px;display:flex;gap:17px}
.dots i{width:8px;height:8px;border-radius:50%;background:var(--white);display:block}
.dots i.on{background:var(--orange)}

/* how it works */
.works-title{top:778px;width:1200px;text-align:center;font-size:44px}
.steps-line{top:950px;left:272px;width:656px;height:3px;background:var(--orange)}
.step{position:absolute;top:870px;width:200px;margin-left:-100px;text-align:center}
.step-photo{width:162px;height:162px;margin:0 auto;border-radius:50%;border:6px solid var(--orange)}
.step h3{margin-top:24px;font-family:"Montserrat",sans-serif;font-weight:700;font-size:18px;color:var(--navy)}
.step p{margin:4px auto 0;width:150px;font-family:"Arimo",sans-serif;font-size:13px;line-height:17px;color:#333}

/* benefits */
.benefits-title{top:1270px;left:138px;font-size:44px}
.arrow{font-family:"Montserrat",sans-serif;font-size:26px}
.benefit{position:absolute;top:1340px;width:230px}
.benefit svg{display:block;height:70px}
.benefit h3{margin-top:16px;font-family:"Oswald",sans-serif;font-weight:400;font-size:26px;line-height:30px;color:var(--navy);height:74px}
.benefit p{font-family:"Arimo",sans-serif;font-size:12.5px;line-height:17px;width:150px;color:#333}

/* who it's for */
.audience{top:1620px;left:0;width:1200px;height:550px;background:linear-gradient(90deg,#f6d6cd 0%,#f2d3cb 50%,#efcfc6 100%)}
.audience-title{top:1690px;left:141px;font-size:44px}
.audience-list{top:1790px;left:152px;font-family:"Oswald",sans-serif;font-size:24px;line-height:58px;color:var(--navy);list-style:none}
.audience-list .on{color:var(--orange)}
.audience-card{top:1761px;left:448px;width:295px;height:342px;background:var(--white);padding:34px 24px;font-size:18px;line-height:24px;color:#222}
.audience-photo{top:1761px;left:743px;width:319px;height:342px;background:linear-gradient(135deg,#3a2a22,#8a5a3c 45%,#d9b89a 75%,#5a4234)}

/* testimonials */
.testi-title{top:2222px;width:1200px;text-align:center;font-size:44px}
.testi-logo{top:2325px;width:1200px;display:flex;justify-content:center;align-items:center;gap:10px;font-family:"Montserrat",sans-serif;font-weight:500;font-size:26px;color:#6b7785}
.testi-logo i{width:26px;height:26px;border-radius:50%;background:#2c9ac9;display:block}
.quote{top:2380px;width:1200px;text-align:center;font-style:italic;font-size:23px;color:var(--navy)}

/* video */
.video-peach{top:2491px;left:0;width:1200px;height:588px;background:var(--peach)}
.video-navy{top:3079px;left:0;width:1200px;height:575px;background:linear-gradient(180deg,#1e3f6b,#183862)}
.video-title{top:2528px;width:1200px;text-align:center;font-size:44px;line-height:52px}
.video-frame{top:2657px;left:172px;width:837px;height:496px;border:2px solid var(--orange)}
.video-still{top:2667px;left:182px;width:836px;height:495px;background:linear-gradient(135deg,#2a3348,#4a5670 45%,#6f7480 70%,#2d3446)}
.play{top:2880px;left:565px}

/* contact form */
.contact-title{top:3315px;left:191px;font-size:31px;color:var(--white)}
.field{position:absolute;border:1.5px solid var(--white);color:var(--white);font-size:15px;padding:10px 16px}

/* footer */
.site-footer{top:3654px;left:0;width:1200px;height:344px;background:linear-gradient(90deg,#ee3e25,#f3723b)}
.footer-brand{top:3700px;left:0;width:1200px;text-align:center;color:var(--white);font-size:27px}
.foot-head{font-family:"Montserrat",sans-serif;font-weight:700;font-size:19px;color:var(--white);top:3772px}
.foot-list{font-size:15px;color:var(--white);line-height:28.5px;top:3810px;list-style:none}
.foot-list li{display:flex;align-items:center;gap:10px}
.foot-list svg{flex:none}
.bottom-bar{top:3998px;left:0;width:1200px;height:40px;background:var(--navy-deep);color:var(--white);font-family:"Arimo",sans-serif;font-size:13px;display:flex;align-items:center;justify-content:center}
</style>
</head>
<body>

<header class="site-nav abs">
  <div class="brand abs">KelvaTrix482</div>
  <nav class="nav-links abs">
    <span class="active">Home</span><span>Product</span><span>Solutions</span><span>ROI / Economics</span><span>Case Studies</span><span>Pricing</span><span>About</span><span>Resources</span><span>Contact</span>
  </nav>
</header>

<div class="page-bg-peach abs"></div>

<section class="hero abs" role="img" aria-label="Row of Pindle cooking robots in a commercial kitchen, navy overlay"></section>
<h1 class="hero-title abs">Meet Pindle — Your New Robotic<br>Chef for High-Volume, Consistent Cooking.</h1>
<p class="hero-sub abs">Increase throughput. Reduce labor. Deliver perfect food every time.</p>
<div class="btn btn-orange" style="left:415px;top:412px;width:188px;height:40px">Request a Demo</div>
<div class="btn btn-navy" style="left:613px;top:412px;width:200px;height:40px">Watch Pindle Cook</div>
<div class="dots abs"><i></i><i class="on"></i><i></i><i></i><i></i></div>

<h2 class="works-title heading abs">How Pindle Works</h2>
<div class="steps-line abs"></div>
<div class="step" style="left:272px"><div class="step-photo" role="img" aria-label="Chef loading ingredients" style="background:linear-gradient(135deg,#2b2b2b,#7a6b5c)"></div><h3>Load Ingredients</h3><p>Lorem ipsum dolor sit amet, consectetur adipiscing elit,</p></div>
<div class="step" style="left:494px"><div class="step-photo" role="img" aria-label="Fresh tomatoes and herbs" style="background:linear-gradient(135deg,#2d4a2a,#c23a22)"></div><h3>Select Recipe</h3><p>Sed do eiusmod tempor incididunt ut labore et dolore magna aliqua.</p></div>
<div class="step" style="left:707px"><div class="step-photo" role="img" aria-label="Pindle cooking robot" style="background:linear-gradient(135deg,#c9ccd1,#5c6068)"></div><h3>Pindle Cooks</h3><p>Lorem ipsum dolor sit amet, consectetur adipiscing elit,</p></div>
<div class="step" style="left:928px"><div class="step-photo" role="img" aria-label="Plated dish served at a table" style="background:linear-gradient(135deg,#3a2226,#b83040)"></div><h3>Serve</h3><p>Sed do eiusmod tempor incididunt ut labore et dolore magna aliqua.</p></div>

<h2 class="benefits-title heading abs">Key Benefits</h2>
<div class="arrow abs" style="left:1010px;top:1287px;color:var(--navy)">‹</div>
<div class="arrow abs" style="left:1052px;top:1287px;color:var(--orange)">›</div>

<div class="benefit" style="left:138px">
  <svg width="76" height="70" viewBox="0 0 76 70" fill="none" stroke="#f04e23" stroke-width="2"><circle cx="14" cy="34" r="6"/><circle cx="38" cy="30" r="7"/><circle cx="62" cy="34" r="6"/><path d="M4 66v-12a10 10 0 0 1 20 0v12M26 66v-14a12 12 0 0 1 24 0v14M52 66v-12a10 10 0 0 1 20 0v12"/></svg>
  <h3>Labor savings</h3><p>Lorem ipsum dolor sit amet, consectetur adipiscing elit,</p></div>
<div class="benefit" style="left:370px">
  <svg width="74" height="70" viewBox="0 0 74 70" fill="none" stroke="#f04e23" stroke-width="2"><circle cx="37" cy="35" r="30" stroke-dasharray="6 3"/><circle cx="37" cy="35" r="20"/><circle cx="37" cy="35" r="11"/><path d="M37 28v7l5 4"/></svg>
  <h3>Zero inconsistency</h3><p>Lorem ipsum dolor sit amet, consectetur adipiscing elit,</p></div>
<div class="benefit" style="left:611px">
  <svg width="74" height="70" viewBox="0 0 74 70" fill="none" stroke="#f04e23" stroke-width="2.5"><path d="M62 22A31 31 0 1 0 66 42"/><path d="M56 14l8 8-10 3"/><text x="37" y="44" text-anchor="middle" fill="#f04e23" stroke="none" font-family="Oswald,sans-serif" font-size="22">24/7</text></svg>
  <h3>24/7 uptime</h3><p>Lorem ipsum dolor sit amet, consectetur adipiscing elit,</p></div>
<div class="benefit" style="left:851px">
  <svg width="66" height="70" viewBox="0 0 66 70" fill="none" stroke="#f04e23" stroke-width="2.5"><path d="M33 4c9 8 12 20 10 38H23C21 24 24 12 33 4z"/><path d="M23 34l-10 12h10M43 34l10 12H43"/><path d="M28 52v8M33 52v10M38 52v8"/><circle cx="33" cy="22" r="3"/></svg>
  <h3>Throughput increases (30–50% faster)</h3><p>Lorem ipsum dolor sit amet, consectetur adipiscing elit,</p></div>

<section class="audience abs" role="img" aria-label="Softly faded restaurant dining room background"></section>
<h2 class="audience-title heading abs">Who It’s For</h2>
<ul class="audience-list abs">
  <li class="on">QSR restaurants</li><li>Fast casual</li><li>Catering/commissaries</li><li>Ghost kitchens</li>
</ul>
<div class="audience-card abs">Lorem ipsum dolor sit amet, consectetur adipiscing elit, sed do eiusmod tempor incididunt ut labore et dolore magna aliqua. Quis ipsum suspendisse ultrices gravida. Risus commodo viverra maecenas accumsan lacus vel facilisis.</div>
<div class="audience-photo abs" role="img" aria-label="Warmly lit restaurant interior with tables and chairs"></div>

<h2 class="testi-title heading abs">Testimonials</h2>
<div class="testi-logo abs"><i></i>Northgrill</div>
<div class="arrow abs" style="left:240px;top:2370px;color:var(--navy)">‹</div>
<p class="quote abs">“Pindle helped us reduce cooking times by 40%.”</p>
<div class="arrow abs" style="left:937px;top:2370px;color:var(--orange)">›</div>

<div class="video-peach abs"></div>
<div class="video-navy abs" role="img" aria-label="Blurred trade show booth background with navy overlay"></div>
<h2 class="video-title heading abs">Watch Pindle cook a full<br>batch from start to finish.</h2>
<div class="video-frame abs"></div>
<div class="video-still abs" role="img" aria-label="Video still of Pindle cooking at a trade show booth"></div>
<svg class="play abs" width="64" height="64" viewBox="0 0 64 64" fill="none" stroke="#fff" stroke-width="2"><circle cx="32" cy="32" r="29"/><path d="M25 19l19 13-19 13z"/></svg>

<div class="btn btn-orange" style="left:517px;top:3204px;width:166px;height:44px">Book a Demo</div>

<h2 class="contact-title heading abs">Get in Touch</h2>
<div class="field" style="left:196px;top:3380px;width:260px;height:39px">Name</div>
<div class="field" style="left:468px;top:3380px;width:261px;height:39px">Email</div>
<div class="field" style="left:747px;top:3377px;width:276px;height:97px">Message</div>
<div class="field" style="left:196px;top:3436px;width:260px;height:39px">Phone</div>
<div class="field" style="left:468px;top:3436px;width:261px;height:39px">Location</div>
<div class="btn btn-orange" style="left:517px;top:3497px;width:166px;height:43px">Submit</div>

<footer class="site-footer abs"></footer>
<div class="brand footer-brand abs">KelvaTrix482</div>

<h4 class="foot-head abs" style="left:147px">Contact Us</h4>
<ul class="foot-list abs" style="left:145px">
  <li><svg width="12" height="14" viewBox="0 0 12 14"><path d="M6 0a5 5 0 0 0-5 5c0 4 5 9 5 9s5-5 5-9a5 5 0 0 0-5-5z" fill="#fff"/><circle cx="6" cy="5" r="2" fill="#f0522a"/></svg>48 Ferncliff Ave, Marlow Bay,</li>
  <li style="padding-left:22px">CA 90412</li>
  <li><svg width="13" height="10" viewBox="0 0 13 10"><rect width="13" height="10" rx="1" fill="#fff"/><path d="M0 1l6.5 5L13 1" stroke="#f0522a" fill="none"/></svg>info@kelvatrix482.com</li>
  <li><svg width="13" height="13" viewBox="0 0 13 13"><path d="M3 0l2 3-1.5 1.5a8 8 0 0 0 5 5L10 8l3 2-1.5 3C6 13 0 7 0 1.5z" fill="#fff"/></svg>+1 [800] 555 0148</li>
</ul>

<h4 class="foot-head abs" style="left:458px">Quick Links</h4>
<ul class="foot-list abs" style="left:456px">
  <li><span>›</span>Home</li><li><span>›</span>Products</li><li><span>›</span>Solutions</li><li><span>›</span>ROI / Economics</li><li><span>›</span>Case Studies</li>
</ul>
<ul class="foot-list abs" style="left:672px">
  <li><span>›</span>Pricing</li><li><span>›</span>About</li><li><span>›</span>Resources</li><li><span>›</span>Contact</li>
</ul>

<h4 class="foot-head abs" style="left:899px">Follow Us</h4>
<ul class="foot-list abs" style="left:897px">
  <li><svg width="12" height="12"><circle cx="6" cy="6" r="6" fill="#fff"/></svg>Socialnest</li>
  <li><svg width="12" height="12"><rect width="12" height="12" rx="2" fill="#fff"/></svg>Workgrid</li>
  <li><svg width="12" height="12"><circle cx="6" cy="6" r="6" fill="#fff"/></svg>Photoloop</li>
  <li><svg width="12" height="12"><rect width="12" height="12" rx="2" fill="#fff"/></svg>Clipstream</li>
</ul>

<div class="bottom-bar abs">© 2025 | www.kelvatrix482.com</div>

</body>
</html>
```